Marlowe Crest Salon needs a product poster

This poster is advertising our products and services. There are several damask patterns throughout the store. Our store's colors are blue, yellow, white, and gold.However the use of vibrant colors would be great! Our theme is old Hollywood. We have to use this design for our price list, product advertisement, and store promotions poster. Poster 2 and 3 can have the same layout. Poster 1 is different because I want the menu enclosed in a frame with the model resting against it or on top of it. All three posters will be hung on the same wall. I have attached my logo and additional photos for your review. I have also attached a images few posters. To give a better idea. I like how the fonts are not all the same. I like how they used the space. I like the use of color. Also I want the logo small with a white oval background. I don't want our logo to be a focal point.
Poster 1: The menu. This poster should include the blonde sailor either above the menu or beside the menu, 2 images have been included to choose from. I want the area with the prices in some type of decorative frame, with the model on top or on the side. (The model is displaying the prices) Also the model's background is white but I want her background to have color. Green would be great! I also like the idea of having "Now Showing" as part of the frame.
The text should read
" Services
Full Body Application..........................................$35.00
Half Body Application.........................................$20.00
Competition Application......................................$50,00
Face Only...........................................................$10.00
Packages:
4 Tans.... ............................................................$120.00 (Never Expires)
8 Tans ................................................................$200.00 (Never Expires)
Monthly Unlimited...............................................$95.00
Specials:
High School Students .......................................$25.00 EVERYDAY!!
All Day Every Tuesday.......................................$25.00
New Clients........................................................$25.00 (First Visit Only)
(If you want to be creative this section can be separate from the menu or part of the menu. Your choice)
Don't have time to come to us? We also have MOBILE Services! OUR ARTISTS CAN COME TO YOU!
In-Home Party Rates (5 people or more)...........$35.00 per person (Travel Fee Waived)
Poster 2: Rapid Solution...The image of the pinup with the clock if for this poster.
The text should read:
" PRESSED FOR TIME? Try our RAPID sunless solution. Rinse in as little as 2 hours" (Pressed for time, Rapid, and 2 Hours is what we want to stand out)
Poster 3: Packages..The image for this poster is of the girl with the binoculars.
The text should read:
"We offer packages and memberships with UNBELIEVABLE SAVINGS. Tans as low as $20!!" (Unbelievable savings and $20 is what we want to stand out)
Updates
I made changes to my briefing. Please let me know if I need to make any other changes or additions
We increased our budget for our design, in order to get more participants
I updated our brief. I have included examples and more detailed instructions. I hope this helps
Target Market(s)
People who value beauty and glamour. We have an upscale clientele.
Industry/Entity Type
Advertising

```html
<!DOCTYPE html>
<html lang="en">
<head>
<meta charset="utf-8">
<title>Marlowe Crest Salon – Packages &amp; Memberships</title>
<link rel="stylesheet" href="https://fonts.googleapis.com/css2?family=Old+Standard+TT:wght@400;700&family=Great+Vibes&display=swap">
<style>
  :root {
    --poster-pink: #eaa8a2;
    --poster-pink-light: #f3c2bc;
    --poster-pink-deep: #d98e88;
    --ink: #1d1717;
    --band-black: #231c1c;
    --cream: #f4efe4;
    --rose-type: #e98c8c;
    --white: #ffffff;
  }
  * { margin: 0; padding: 0; box-sizing: border-box; }
  html, body { width: 960px; height: 1200px; overflow: hidden; }
  body { background: var(--poster-pink); }

  .poster {
    position: relative;
    width: 960px;
    height: 1200px;
    overflow: hidden;
    background:
      radial-gradient(ellipse at 50% 40%, var(--poster-pink-light) 0%, var(--poster-pink) 55%, var(--poster-pink-deep) 100%);
    font-family: "Old Standard TT", "Times New Roman", serif;
    color: var(--ink);
  }

  .damask-ornament {
    position: absolute;
    left: 24px;
    top: 190px;
    width: 340px;
    height: 410px;
    border-radius: 48% 40% 30% 50%;
    background: radial-gradient(ellipse at 45% 50%, #2b2020 0%, #3a2a2a 60%, rgba(58,42,42,0) 100%);
  }

  .model-photo {
    position: absolute;
    left: 216px;
    top: 0;
    width: 612px;
    height: 672px;
    border-radius: 40% 40% 0 0;
    background: linear-gradient(180deg, #e6b49a 0%, #d9a38a 25%, #4f6f9c 45%, #a9bcd6 75%, #dfe4ec 100%);
  }

  .intro-strip {
    position: absolute;
    left: 96px;
    top: 518px;
    width: 786px;
    height: 122px;
    background: var(--cream);
    box-shadow: 0 2px 6px rgba(0,0,0,0.15);
    display: flex;
    flex-direction: column;
    justify-content: center;
    align-items: center;
    text-align: center;
  }
  .intro-strip p {
    font-size: 34px;
    letter-spacing: 6px;
    line-height: 46px;
    text-transform: uppercase;
  }

  .savings-band {
    position: absolute;
    left: 66px;
    top: 666px;
    width: 822px;
    height: 114px;
    background: var(--band-black);
    transform: rotate(-0.6deg);
  }
  .savings-band .headline {
    display: block;
    text-align: center;
    font-size: 70px;
    letter-spacing: 9px;
    line-height: 114px;
    color: var(--rose-type);
    text-transform: uppercase;
  }

  .savings-plate {
    position: absolute;
    left: 104px;
    top: 766px;
    width: 760px;
    height: 186px;
    background: var(--band-black);
  }
  .savings-plate::after {
    content: "";
    position: absolute;
    inset: 14px 14px 14px 14px;
    border: 2px solid var(--cream);
    pointer-events: none;
  }
  .savings-script {
    position: absolute;
    left: 0;
    right: 0;
    top: 728px;
    text-align: center;
    font-family: "Great Vibes", cursive;
    font-size: 210px;
    line-height: 1;
    color: var(--white);
  }

  .price-line {
    position: absolute;
    left: 120px;
    top: 992px;
    font-size: 32px;
    letter-spacing: 6px;
    text-transform: uppercase;
  }
  .price-box {
    position: absolute;
    left: 528px;
    top: 948px;
    width: 372px;
    height: 144px;
    background: var(--cream);
    border: 4px solid var(--ink);
    box-shadow: 0 2px 6px rgba(0,0,0,0.2);
    display: flex;
    align-items: center;
    justify-content: center;
  }
  .price-box::after {
    content: "";
    position: absolute;
    inset: 8px;
    border: 2px solid var(--ink);
  }
  .price-box span {
    font-size: 100px;
    letter-spacing: 12px;
    line-height: 1;
  }

  .brand-mark {
    position: absolute;
    left: 782px;
    top: 1118px;
    width: 168px;
    height: 64px;
    border-radius: 50%;
    background: var(--white);
    display: flex;
    align-items: center;
    justify-content: center;
    text-align: center;
    font-size: 15px;
    line-height: 17px;
    color: var(--ink);
    padding: 0 18px;
  }
</style>
</head>
<body>
  <main class="poster">
    <div class="damask-ornament" role="img" aria-label="Black damask scroll ornament"></div>
    <div class="model-photo" role="img" aria-label="Pin-up model in a denim dress looking through red binoculars while holding an open laptop"></div>

    <section class="intro-strip">
      <p>We offer packages and</p>
      <p>memberships with</p>
    </section>

    <div class="savings-band">
      <span class="headline">Unbelievable</span>
    </div>
    <div class="savings-plate"></div>
    <h1 class="savings-script">Savings</h1>

    <p class="price-line">Tans as low as</p>
    <div class="price-box"><span>$20!!</span></div>

    <div class="brand-mark">Marlowe Crest Salon</div>
  </main>
</body>
</html>
```